"Harrow Crest Builders" is a residential building company and needs a new business card design and may re

We would like a redesign based on the existing logo, and would like to see a new font as well. We are bespoke home builders who build sustainable energy efficient homes.

Industry/Entity Type

Construction

Contact Information for Business Card

Business card size 40mm x 90mm

Colors

Designer to choose colors to be used in the design.

```html
<!DOCTYPE html>
<html lang="en">
<head>
<meta charset="utf-8">
<title>Harrow Crest Builders — Business Cards</title>
<link href="https://fonts.googleapis.com/css2?family=Open+Sans:wght@400;700&display=swap" rel="stylesheet">
<style>
  :root {
    --backdrop: #3a322d;
    --card: #151515;
    --card-edge: #1f1f1f;
    --ink: #f2f2f2;
    --ink-soft: #9a9a9a;
    --accent: #9cc23c;
    --rule: #8a8a8a;
  }
  * { box-sizing: border-box; margin: 0; padding: 0; }
  html, body {
    width: 1200px;
    height: 864px;
    overflow: hidden;
  }
  body {
    background: var(--backdrop);
    font-family: "Open Sans", Arial, sans-serif;
    color: var(--ink);
    position: relative;
  }
  .card {
    position: absolute;
    width: 540px;
    height: 310px;
    background: var(--card);
    border: 1px solid var(--card-edge);
    box-shadow: 0 12px 30px rgba(0, 0, 0, 0.45);
  }
  .card--front { left: 70px; top: 90px; }
  .card--back  { left: 590px; top: 450px; width: 560px; height: 320px; }

  .brand {
    display: flex;
    align-items: center;
    gap: 12px;
  }
  .brand__mark {
    width: 26px;
    height: 26px;
    background: var(--accent);
    flex: none;
  }
  .brand__name {
    font-weight: 700;
    font-size: 30px;
    letter-spacing: -0.5px;
    line-height: 1;
  }
  .card--front .brand {
    position: absolute;
    left: 70px;
    top: 110px;
  }
  .card--front .brand__name { color: #c9c9c9; }
  .front__web {
    position: absolute;
    left: 70px;
    top: 222px;
    font-size: 13px;
    letter-spacing: 3px;
    color: var(--ink-soft);
  }

  .card--back .brand {
    position: absolute;
    right: 34px;
    top: 112px;
  }
  .card--back .brand__name { font-size: 24px; color: var(--ink); }
  .card--back .brand__mark { width: 20px; height: 20px; }

  .contact {
    position: absolute;
    left: 36px;
    top: 88px;
    font-size: 13.5px;
    line-height: 19px;
  }
  .contact__name {
    color: var(--accent);
    font-weight: 700;
    font-size: 15px;
    text-transform: uppercase;
    margin-bottom: 4px;
  }
  .contact__row {
    display: flex;
    align-items: center;
    gap: 7px;
  }
  .contact__row svg { width: 11px; height: 11px; flex: none; }
  .contact__icon-space { width: 11px; flex: none; }

  .divider {
    position: absolute;
    left: 36px;
    right: 28px;
    top: 168px;
    height: 1px;
    background: var(--rule);
  }
  .contact__reach { margin-top: 15px; }

  .address {
    position: absolute;
    right: 34px;
    bottom: 30px;
    text-align: right;
    font-size: 14.5px;
    line-height: 20px;
  }
</style>
</head>
<body>

<section class="card card--front" aria-label="Business card front">
  <div class="brand">
    <span class="brand__mark"></span>
    <span class="brand__name">Harrow Crest Builders</span>
  </div>
  <p class="front__web">www.harrowcrestbuilders.com.au</p>
</section>

<section class="card card--back" aria-label="Business card back">
  <div class="contact">
    <p class="contact__name">Daniel Marsh</p>
    <p>Registration 40318</p>
    <p>ABN: 52 904 317 268</p>
    <div class="contact__reach">
      <p class="contact__row">
        <svg viewBox="0 0 12 12" aria-hidden="true"><rect x="3" y="0.8" width="6" height="10.4" rx="1" fill="none" stroke="var(--accent)" stroke-width="1.3"/><circle cx="6" cy="9.3" r="0.7" fill="var(--accent)"/></svg>
        <span>0400 555 018</span>
      </p>
      <p class="contact__row">
        <svg viewBox="0 0 12 12" aria-hidden="true"><rect x="0.8" y="2.5" width="10.4" height="7" fill="none" stroke="var(--accent)" stroke-width="1.3"/><path d="M0.8 2.8 6 6.6 11.2 2.8" fill="none" stroke="var(--accent)" stroke-width="1.2"/></svg>
        <span>daniel@harrowcrestbuilders.com.au</span>
      </p>
      <p class="contact__row">
        <svg viewBox="0 0 12 12" aria-hidden="true"><circle cx="6" cy="6" r="5.4" fill="var(--accent)"/><path d="M0.8 6h10.4M6 0.8c2.4 2.6 2.4 7.8 0 10.4M6 0.8c-2.4 2.6-2.4 7.8 0 10.4" fill="none" stroke="var(--card)" stroke-width="0.9"/></svg>
        <span>www.harrowcrestbuilders.com.au</span>
      </p>
    </div>
  </div>

  <div class="brand">
    <span class="brand__mark"></span>
    <span class="brand__name">Harrow Crest Builders</span>
  </div>

  <div class="divider"></div>

  <address class="address" style="font-style:normal">
    Harrow Crest Builders Pty Ltd<br>
    PO Box 4120<br>
    Northgate<br>
    LPO Ashford WA 6099
  </address>
</section>

</body>
</html>
```